Business cards and Stationary for Bright Learning Alliance
A Chinese Education Consulting Company
Business cards and Stationary for Bright Learning Alliance - Education
Creative Brief
Professional
Dennis R. Tolwy
Manager
7214 Marlow Court, San Ramon, CA 94583
dennistolwy@brilearnal.com
www.brilearnal.com
Please leave abundant space for multi address, (2) multi cell phones (3)

```html
<!DOCTYPE html>
<html lang="en">
<head>
<meta charset="utf-8">
<title>Bright Learning Alliance – Business Cards</title>
<link href="https://fonts.googleapis.com/css2?family=Open+Sans:wght@400;600;700&family=Cinzel:wght@700&display=swap" rel="stylesheet">
<style>
  :root{
    --bg:#eceef0;
    --card:#ffffff;
    --red:#c8141c;
    --red-dark:#8e0a10;
    --gold:#c9a24a;
    --gold-light:#ecd596;
    --ink:#3a3a3a;
    --muted:#777777;
    --faint:#f1dede;
  }
  *{margin:0;padding:0;box-sizing:border-box}
  html,body{width:1200px;height:1009px;overflow:hidden;background:var(--bg)}
  .canvas{position:relative;width:1200px;height:1009px}
  .card{position:absolute;width:805px;height:460px;background:var(--card);border-radius:26px;overflow:hidden;box-shadow:0 6px 22px rgba(0,0,0,.12)}
  .card--back{left:330px;top:30px}
  .card--front{left:65px;top:519px}

  .back-url{position:absolute;left:40px;top:60px;font-family:'Open Sans',sans-serif;font-weight:700;font-style:normal;font-size:26px;letter-spacing:4px;color:var(--red)}
  .back-mark{position:absolute;right:60px;top:120px;width:360px;height:280px;display:flex;flex-direction:column;align-items:center;justify-content:center;gap:18px}
  .back-mark .dot{width:130px;height:130px;border-radius:50%;background:var(--faint)}
  .back-mark .name{font-family:'Cinzel',serif;font-weight:700;font-size:26px;color:var(--faint);text-align:center}

  .front-wave{position:absolute;left:0;bottom:0;width:805px;height:260px}
  .front-mark{position:absolute;left:40px;top:60px;width:250px;display:flex;flex-direction:column;align-items:center;gap:14px}
  .front-mark .dot{width:110px;height:110px;border-radius:50%;background:var(--red)}
  .front-mark .name{font-family:'Cinzel',serif;font-weight:700;font-size:19px;color:var(--red);text-align:center;line-height:1.25}
  .divider{position:absolute;left:318px;top:70px;width:1px;height:190px;background:#cfcfcf}
  .contact{position:absolute;left:338px;top:70px;font-family:'Open Sans',sans-serif;color:var(--ink)}
  .contact .person{font-weight:700;font-size:19px;color:var(--red)}
  .contact .role{font-size:13px;color:var(--muted);margin-bottom:12px}
  .contact ul{list-style:none}
  .contact li{display:flex;align-items:center;gap:9px;font-size:14px;line-height:24px}
  .contact svg{width:15px;height:15px;flex:none}
</style>
</head>
<body>
<main class="canvas">

  <section class="card card--back" aria-label="Card back">
    <p class="back-url">www.brilearnal.com</p>
    <div class="back-mark">
      <span class="dot"></span>
      <span class="name">Bright Learning Alliance</span>
    </div>
  </section>

  <section class="card card--front" aria-label="Card front">
    <svg class="front-wave" viewBox="0 0 805 260" preserveAspectRatio="none" aria-hidden="true">
      <defs>
        <linearGradient id="redFill" x1="0" y1="0" x2="1" y2="0">
          <stop offset="0" stop-color="#8e0a10"/>
          <stop offset=".35" stop-color="#e0222a"/>
          <stop offset="1" stop-color="#b0121a"/>
        </linearGradient>
        <linearGradient id="goldFill" x1="0" y1="0" x2="1" y2="0">
          <stop offset="0" stop-color="#b88a34"/>
          <stop offset=".5" stop-color="#ecd596"/>
          <stop offset="1" stop-color="#c9a24a"/>
        </linearGradient>
      </defs>
      <path d="M0 40 C220 130 420 200 805 150 L805 260 L0 260 Z" fill="url(#goldFill)"/>
      <path d="M0 70 C220 160 430 220 805 175 L805 260 L0 260 Z" fill="#ffffff"/>
      <path d="M0 85 C200 190 420 235 805 195 L805 260 L0 260 Z" fill="url(#redFill)"/>
      <path d="M0 215 C260 250 520 215 805 225" stroke="url(#goldFill)" stroke-width="5" fill="none"/>
    </svg>

    <div class="front-mark">
      <span class="dot"></span>
      <span class="name">Bright Learning Alliance</span>
    </div>

    <div class="divider"></div>

    <div class="contact">
      <p class="person">Dennis R. Tolwy</p>
      <p class="role">Manager</p>
      <ul>
        <li><svg viewBox="0 0 16 16"><circle cx="8" cy="8" r="8" fill="#c8141c"/><path d="M8 3.5a3 3 0 0 0-3 3c0 2.2 3 6 3 6s3-3.8 3-6a3 3 0 0 0-3-3z" fill="#fff"/></svg>7214 Marlow Court, San Ramon, CA 94583</li>
        <li><svg viewBox="0 0 16 16"><circle cx="8" cy="8" r="8" fill="#c8141c"/><path d="M5 4h2l1 2.5-1.2.8a6 6 0 0 0 2 2l.8-1.2L12 9v2c-4 .5-7.5-3-7-7z" fill="#fff"/></svg>+1 925-555-0142</li>
        <li><svg viewBox="0 0 16 16"><circle cx="8" cy="8" r="8" fill="#c8141c"/><rect x="5.5" y="3.5" width="5" height="9" rx="1" fill="#fff"/></svg>+1 888-555-0178</li>
        <li><svg viewBox="0 0 16 16"><circle cx="8" cy="8" r="8" fill="#c8141c"/><rect x="4" y="5" width="8" height="6" fill="#fff"/><path d="M4 5l4 3.5L12 5" stroke="#c8141c" fill="none"/></svg>dennistolwy@brilearnal.com</li>
        <li><svg viewBox="0 0 16 16"><circle cx="8" cy="8" r="8" fill="#c8141c"/><circle cx="8" cy="8" r="4" stroke="#fff" fill="none"/><path d="M4 8h8M8 4v8" stroke="#fff"/></svg>www.brilearnal.com</li>
      </ul>
    </div>
  </section>

</main>
</body>
</html>
```